Design and code ShopVantel website

Website is currently up and running but looking for a fresh and new theme or design for it.

Must interact perfectly with ShopVantel

Will provide plenty of images.

All content should stay exactly the same as far as text and information.

Looking for a dark but elegant theme. All of the information necessary is listed.

Will need detailed instructions on how to implement the website into our current system... simply looking to make our page unique and not just a stock ShopVantel theme

Coding

Coded - Design and coding required

Number of Pages Required

5+ page

Colors
000000
9d9d9d
ffffff

Requirements
Must have
• same information as www.morvellinavapors.example

```html
<!DOCTYPE html>
<html lang="en">
<head>
<meta charset="utf-8">
<title>Morvellina Vapors</title>
<link rel="stylesheet" href="https://fonts.googleapis.com/css2?family=Poiret+One&family=Oswald:wght@400&family=Open+Sans:wght@400;700&display=swap">
<style>
:root{
  --gold:#f4b913;
  --black:#000000;
  --wood:#1b1b1b;
  --grey:#9d9d9d;
  --white:#ffffff;
  --amber:#8a6422;
  --cream:#d9cdb4;
  --crust:#6b4a26;
}
*{box-sizing:border-box;margin:0;padding:0}
html,body{width:1025px;height:1200px;overflow:hidden}
body{position:relative;background:linear-gradient(180deg,#141414 0%,#1f1f1f 35%,#1a1a1a 60%,#202020 100%);font-family:"Open Sans",Arial,sans-serif;color:var(--white)}
.abs{position:absolute}
.thin{font-family:"Poiret One",cursive}

/* header */
.phone-top{left:213px;top:17px;font-size:12px;display:flex;align-items:center;gap:5px;font-family:"Poiret One",cursive;font-weight:400}
.social-top{left:213px;top:40px;display:flex;gap:6px}
.social-top span{width:7px;height:7px;border-radius:50%;background:var(--gold)}
.brand{left:413px;top:12px;width:200px;text-align:center;font-family:"Poiret One",cursive;font-size:22px;color:var(--white);line-height:30px}
.account{left:739px;top:20px;font-size:9px;font-family:"Poiret One",cursive}
.account .cart{display:block;width:7px;height:6px;background:var(--gold);margin-bottom:3px}

/* nav */
.nav{left:0;top:80px;width:1025px;height:24px;border-top:1px solid var(--gold);border-bottom:1px solid var(--gold)}
.nav ul{position:absolute;left:213px;top:0;display:flex;list-style:none;height:22px}
.nav li{font-family:"Oswald",sans-serif;font-size:8px;line-height:22px;padding:0 6px;color:var(--white)}
.nav li.active{background:var(--gold)}
.search{right:213px;top:0;width:25px;height:22px;background:var(--gold);display:flex;align-items:center;justify-content:center}

/* hero */
.hero-title{left:213px;top:183px;font-size:19px;font-weight:400}
.hero-text{left:213px;top:224px;width:235px;font-size:7px;line-height:12px;color:#eee}
.offer{left:213px;top:301px;width:176px;height:54px;border:1px solid var(--gold);padding:8px 0 0 28px}
.offer .name{font-size:13px}
.offer .row{display:flex;align-items:center;gap:6px;margin-top:1px}
.offer .price{font-size:13px}
.btn{background:var(--gold);color:#111;font-family:"Oswald",sans-serif;text-align:center;text-transform:uppercase}
.offer .btn{width:65px;height:17px;font-size:10px;line-height:17px}
.photo-circle{border-radius:50%;border:1.5px solid #4a4a4a}
.photo-small{background:radial-gradient(circle at 50% 60%,#b08a3c 0%,#6b4a26 30%,#d8ccb6 48%,#2a2016 68%,#0b0b0b 100%)}
.photo-large{background:radial-gradient(circle at 50% 55%,#c79a3e 0%,#8a6422 28%,#c9b79a 45%,#3a2a1a 65%,#0d0d0d 100%)}

/* categories */
.cats{left:213px;top:401px;width:156px;height:237px;background:#121212}
.cats h3{font-family:"Poiret One",cursive;font-weight:400;color:var(--gold);font-size:12px;text-align:center;padding:7px 0 5px;border-bottom:1px solid var(--gold)}
.cats ul{list-style:none;border-right:2px solid #2c2c2c;margin-top:4px}
.cats li{font-family:"Poiret One",cursive;font-size:7.5px;height:14.3px;line-height:14px;border-bottom:1px solid #262626;padding-left:19px;position:relative}
.cats li:before{content:"›";position:absolute;left:10px}
.cats li:first-child{border-right:2px solid var(--gold);margin-right:-2px}

/* products */
.section-title{font-family:"Poiret One",cursive;color:var(--gold);font-weight:400}
.products-title{left:389px;top:398px;font-size:19px}
.card{top:433px;width:206px;height:183px;border:1px solid #cfcfcf;text-align:center}
.card .img{height:95px;background:linear-gradient(180deg,#000 0%,#0a0a0a 35%,#5b4424 60%,#8d7650 78%,#2a2218 100%)}
.card .name{font-family:"Poiret One",cursive;font-size:13px;margin-top:8px}
.card .price{font-family:"Poiret One",cursive;font-size:18px;color:var(--gold);margin-top:4px}
.card .btn{width:135px;height:22px;line-height:22px;font-size:10px;margin:5px auto 0}
.dots{left:582px;top:631px;display:flex;gap:5px}
.dots span{width:7px;height:7px;background:var(--white)}
.dots span.on{background:var(--gold)}

/* newsletter */
.newsletter{left:0;top:664px;width:1025px;height:221px;background:linear-gradient(180deg,#0b0b0b,#1e1e1e 50%,#0f0f0f)}
.news-img-left{left:0;top:34px;width:322px;height:187px;background:linear-gradient(90deg,#d8ccb4 0%,#7a5a2c 18%,#b68a3a 32%,#c9b9a0 45%,#8a6422 62%,#2a2016 85%,#0e0e0e 100%)}
.news-img-right{left:690px;top:38px;width:335px;height:183px;background:linear-gradient(90deg,#0e0e0e 0%,#2a2016 20%,#a37a34 40%,#6b4a26 62%,#8a7a4a 78%,#5a3e20 100%)}
.news-title{left:0;width:1025px;top:40px;font-size:31px;text-align:center}
.field{background:#d8d8d8;color:#555;font-size:7px;font-style:italic;padding-left:7px;line-height:19px;height:19px;width:262px;left:381px}
.news-btn{left:445px;top:151px;width:134px;height:22px;line-height:22px;font-size:10px}

/* contact */
.block-title{font-size:21px;top:920px}
.label{font-weight:700;color:var(--gold);font-size:10px;display:flex;align-items:center;gap:5px}
.value{font-family:"Poiret One",cursive;font-size:9px;color:var(--grey);line-height:8px}
.social-foot{left:212px;top:1129px;display:flex;gap:7px}
.social-foot span{width:20px;height:20px;border-radius:50%;background:var(--gold)}
.line-field{border-bottom:1px solid #777;font-size:6px;color:#ccc;padding-bottom:3px}
.send{left:457px;top:1127px;width:134px;height:22px;line-height:22px;font-size:10px}

/* footer */
.footer{left:0;top:1177px;width:1025px;height:23px;background:var(--gold);color:#222;font-family:"Oswald",sans-serif;font-size:6.5px}
.footer .copy{position:absolute;left:213px;top:7px}
.footer ul{position:absolute;right:213px;top:7px;display:flex;gap:11px;list-style:none}
</style>
</head>
<body>

<header>
  <div class="abs phone-top">
    <svg width="6" height="9" viewBox="0 0 6 9"><rect x="0.5" y="0.5" width="5" height="8" rx="1" fill="none" stroke="#f4b913"/></svg>
    <span>5550142236</span>
  </div>
  <div class="abs social-top"><span></span><span></span><span></span></div>
  <div class="abs brand">Morvellina Vapors</div>
  <div class="abs account"><span class="cart"></span>My Account &nbsp;Sign in</div>
</header>

<nav class="abs nav">
  <ul>
    <li class="active">Home</li><li>Wholesale</li><li>Why Choose Us?</li><li>CPSC Info</li><li>Terms &amp; Conditions</li><li>Shipping &amp; Returns</li><li>Contact</li>
  </ul>
  <div class="abs search">
    <svg width="10" height="10" viewBox="0 0 10 10"><circle cx="4" cy="4" r="3" fill="none" stroke="#111" stroke-width="1.5"/><line x1="6.2" y1="6.2" x2="9" y2="9" stroke="#111" stroke-width="1.6"/></svg>
  </div>
</nav>

<section class="hero">
  <h1 class="abs hero-title thin">Welcome to Morvellina Vapors</h1>
  <p class="abs hero-text">Lorem Ipsum is simply dummy text of the printing and typesetting industry. Lorem Ipsum has been the industry's standard dummy text ever since the 1500s, when an unknown printer tookLorem Ipsum is simply dummy text of the printing and typesetting industry. Lorem Ipsum has been the industry's</p>
  <div class="abs offer">
    <div class="name thin">Velvet Crema Reserve</div>
    <div class="row"><span class="price thin">$19.99</span><span class="btn">Buy</span></div>
  </div>
  <div class="abs photo-circle photo-small" style="left:457px;top:213px;width:168px;height:168px" role="img" aria-label="Product photo: a dropper bottle beside cream-filled pastries"></div>
  <div class="abs photo-circle photo-large" style="left:583px;top:137px;width:224px;height:224px" role="img" aria-label="Product photo: three dropper bottles with filled pastries"></div>
</section>

<aside class="abs cats">
  <h3>Categories</h3>
  <ul>
    <li>Asparagus</li><li>Apples</li><li>Avacado</li><li>Alfalfa</li><li>Acorn squash &nbsp;(on 'S')</li><li>Almond</li><li>Arugala</li><li>Artichoke</li><li>Applesauce</li><li>Asian noodles (NOPE, on 'N')</li><li>Antelope</li><li>Ahi tuna (NOPE, this is actually a '')</li><li>Albacore tuna</li><li>Apple juice</li>
  </ul>
</aside>

<section class="products">
  <h2 class="abs products-title section-title">Popular Products</h2>
  <div class="abs card" style="left:385px">
    <div class="img" role="img" aria-label="Product photo: three bottles with pastries and pistachios"></div>
    <div class="name">Velvet Crema Reserve</div>
    <div class="price">$ &nbsp;19.99</div>
    <div class="btn">Choose Options</div>
  </div>
  <div class="abs card" style="left:606px">
    <div class="img" role="img" aria-label="Product photo: three bottles with pastries and pistachios"></div>
    <div class="name" style="margin-top:11px">Velvet Crema Reserve</div>
    <div class="price">$ &nbsp;19.99</div>
    <div class="btn">Choose Options</div>
  </div>
  <div class="abs dots"><span></span><span class="on"></span><span></span></div>
</section>

<section class="abs newsletter">
  <div class="abs news-img-left" role="img" aria-label="Photo: three dropper bottles with cream pastries"></div>
  <div class="abs news-img-right" role="img" aria-label="Photo: bottles with pastries and pistachios"></div>
  <h2 class="abs news-title section-title">Newsletter</h2>
  <div class="abs field" style="top:88px">Name :</div>
  <div class="abs field" style="top:120px">Email :</div>
  <div class="abs btn news-btn">Choose Options</div>
</section>

<section class="address">
  <h2 class="abs block-title section-title" style="left:212px">ADDRESS</h2>
  <div class="abs label" style="left:212px;top:964px">
    <svg width="6" height="9" viewBox="0 0 6 9"><rect x="0.5" y="0.5" width="5" height="8" rx="1" fill="none" stroke="#f4b913"/></svg>Phone :</div>
  <div class="abs value" style="left:212px;top:985px">+10005550187</div>
  <div class="abs label" style="left:212px;top:1013px">
    <svg width="10" height="7" viewBox="0 0 10 7"><rect width="10" height="7" fill="#f4b913"/><path d="M0 0L5 4L10 0" fill="none" stroke="#1b1b1b"/></svg>Email :</div>
  <div class="abs value" style="left:212px;top:1031px">hello@morvellina.example</div>
  <div class="abs label" style="left:212px;top:1060px">
    <svg width="7" height="10" viewBox="0 0 7 10"><path d="M3.5 10L0.5 4.5A3 3 0 1 1 6.5 4.5Z" fill="#f4b913"/><circle cx="3.5" cy="3.5" r="1.2" fill="#1b1b1b"/></svg>Address :</div>
  <div class="abs value" style="left:212px;top:1079px">PO Box 4410 Larkmoor Lane<br>Eastfield Valley 0000 Norland</div>
  <div class="abs social-foot"><span></span><span></span><span></span></div>
</section>

<section class="contact">
  <h2 class="abs block-title section-title" style="left:455px">CONTACT US</h2>
  <div class="abs line-field" style="left:451px;top:962px;width:165px">Name :</div>
  <div class="abs line-field" style="left:629px;top:962px;width:183px">Email :</div>
  <div class="abs line-field" style="left:451px;top:1006px;width:361px">Phone :</div>
  <div class="abs line-field" style="left:451px;top:1094px;width:361px">Message :</div>
  <div class="abs btn send">Send</div>
</section>

<footer class="abs footer">
  <span class="copy">Copyright 2016 Morvellina Vapors.</span>
  <ul><li>Home</li><li>Wholesale</li><li>Why Choose Us?</li><li>CPSC Info</li><li>Terms &amp; Conditions</li><li>Shipping &amp; Returns</li><li>Contact</li></ul>
</footer>

</body>
</html>
```